Brochure Design Project - KelvoraPartners.com.au

Hi,

I am establishing a new business in professional services for "www.KelvoraPartners.com.au".

The website is currently getting developed, so in the interim I would like a e-brochure to send out to my clients.

I have attached a draft layout/content for the brochure.

Please use the same content, in the same order - but i would like some creative in put on the remainder.

Target Market(s)

Financial Advisers, Accountants, Lawyers

Industry/Entity Type

Business

Requirements
Must have
• - must be modern and engaging to look at.
- attached is the colour scheme for the website. Please limit the colours/fonts/format to match the brand of KelvoraPartners.com.au

- on the home page I need to have space for imbedding two youtube video's. The video's will be completed within a week, so I can provide the links then.

- if you do know know how to imbed video's into a PDF brochure, please leave it out.

```html
<!DOCTYPE html>
<html lang="en">
<head>
<meta charset="utf-8">
<title>KelvoraPartners.com.au – Brochure Pages 3 &amp; 4</title>
<link href="https://fonts.googleapis.com/css2?family=Roboto:wght@400;700&display=swap" rel="stylesheet">
<style>
  :root {
    --stage: #5f5f61;
    --paper: #ffffff;
    --orange: #f28a1e;
    --orange-light: #f7a640;
    --orange-deep: #e4711a;
    --heading: #8b5a2b;
    --body: #3f3f3f;
    --bullet: #f28a1e;
    --page-label: #ffffff;
  }
  * { box-sizing: border-box; margin: 0; padding: 0; }
  html, body { width: 1200px; height: 857px; overflow: hidden; }
  body {
    background: var(--stage);
    font-family: "Roboto", Arial, sans-serif;
    position: relative;
  }
  .page {
    position: absolute;
    top: 17px;
    width: 564px;
    height: 798px;
    background: var(--paper);
    overflow: hidden;
  }
  .page--three { left: 29px; }
  .page--four { left: 608px; }

  .brand {
    position: absolute;
    left: 23px; top: 45px;
    height: 44px;
    display: flex; align-items: center; gap: 8px;
  }
  .brand__mark {
    width: 34px; height: 34px;
    background: var(--orange);
    border-radius: 3px;
  }
  .brand__name {
    font-size: 17px; font-weight: 700;
    color: var(--orange);
  }
  .header-band { position: absolute; left: 287px; top: 40px; width: 277px; height: 52px; }
  .footer-band { position: absolute; left: 0; bottom: 0; width: 564px; height: 90px; }
  .footer-url {
    position: absolute; left: 0; right: 0; bottom: 22px;
    text-align: center;
    color: #fff; font-weight: 700; font-size: 17px;
    letter-spacing: 3px;
  }

  .column { position: absolute; top: 170px; width: 227px; }
  .column--left { left: 36px; }
  .column--right { left: 300px; }
  .column--right-narrow { left: 300px; }

  h2 {
    font-size: 13.5px; font-weight: 700;
    color: var(--heading);
    margin-bottom: 16px;
    line-height: 18px;
  }
  .column p {
    font-size: 10.6px; line-height: 19px;
    color: var(--body);
    text-align: justify;
    margin-bottom: 9px;
  }
  .column p.tight { margin-bottom: 0; }
  .column--right p:first-child { margin-top: 34px; }
  .section-gap { margin-top: 26px; }
  .stat-list { list-style: none; margin: 2px 0 12px; }
  .stat-list li {
    font-size: 10.6px; line-height: 12.5px; color: var(--body);
  }
  .stat-list li::before { content: "• "; color: var(--bullet); }
  .home-feature { margin-left: 5px; }

  .page-number {
    position: absolute; top: 824px;
    width: 564px; text-align: center;
    font-size: 25px; color: var(--page-label);
  }
  .page-number--three { left: 29px; }
  .page-number--four { left: 608px; }
</style>
</head>
<body>

<section class="page page--three">
  <div class="brand"><span class="brand__mark"></span><span class="brand__name">KelvoraPartners.com.au</span></div>
  <svg class="header-band" viewBox="0 0 277 52" aria-hidden="true">
    <polygon points="36,0 277,0 277,52 0,52" fill="var(--orange)"/>
    <polygon points="60,0 170,0 130,52 20,52" fill="var(--orange-light)" opacity=".6"/>
    <polygon points="180,0 277,0 277,30 150,30" fill="var(--orange-deep)" opacity=".5"/>
  </svg>

  <div class="column column--left">
    <h2>Client Matching Service</h2>
    <p>The Client Matching Service is based on a highly sophisticated algorithm and is the backbone of KelvoraPartners. It ensures that advisers are provided with leads from clients that actually want their advice!</p>
    <p>When a clients wants to be contacted with quotes from advisers, they can submit an ‘Advice Request’ through the system.</p>
    <p>The ‘Advice Request’ is a two-minute form, which allows the client to share details on the type of adviser they want, a brief description of their professional problem and a budget for the work.</p>
    <p>KelvoraPartners uses the information on the ‘Advice Request’ and compares it to data on all the ‘Adviser Profiles’ on the system to find the top 5 advisers.</p>
    <p>If more than 5 advisers meet the same criteria, the system will then find the top 5 advisers based on their recommendations.</p>
  </div>
  <div class="column column--right">
    <p>The matched advisers will be immediately notified via email. They will have 2 business days to review the ‘Advice Request’ and contact the client. If the adviser fails to contact the client, the next suitable adviser is notified.</p>
    <p>The contact details of the client will remain anonymous. If the adviser is able assist the client upon reviewing the ‘Advice Request’, they can click the ‘Contact’ button and the contact details will be made available.</p>
    <p>The Key Differentiator between KelvoraPartners is that the adviser has the ability to self assess their leads and there is no obligation to proceed.</p>
  </div>

  <svg class="footer-band" viewBox="0 0 564 90" preserveAspectRatio="none" aria-hidden="true">
    <rect width="564" height="90" fill="var(--orange)"/>
    <polygon points="0,0 90,0 40,90 0,90" fill="var(--orange-deep)" opacity=".5"/>
    <rect x="150" y="0" width="14" height="90" fill="var(--orange-light)" opacity=".5"/>
    <rect x="330" y="10" width="30" height="80" fill="var(--orange-light)" opacity=".4"/>
    <rect x="470" y="0" width="10" height="90" fill="var(--orange-deep)" opacity=".4"/>
  </svg>
  <div class="footer-url">www.KelvoraPartners.com.au</div>
</section>

<section class="page page--four">
  <div class="brand"><span class="brand__mark"></span><span class="brand__name">KelvoraPartners.com.au</span></div>
  <svg class="header-band" viewBox="0 0 277 52" aria-hidden="true">
    <polygon points="36,0 277,0 277,52 0,52" fill="var(--orange)"/>
    <polygon points="60,0 170,0 130,52 20,52" fill="var(--orange-light)" opacity=".6"/>
    <polygon points="180,0 277,0 277,30 150,30" fill="var(--orange-deep)" opacity=".5"/>
  </svg>

  <div class="column column--left">
    <h2>Blog</h2>
    <p class="tight">KelvoraPartners has also been developed to serve as a central education centre for clients. We want clients to use KelvoraPartners as the first place to ask questions and retrieve invaluable information about the related industries.</p>
    <p class="tight">We have therefore opened up our ‘Blog’ to allow advisers to publish information such as ‘market commentaries’, journals, presentations, video’s and so forth. The aim is for advisers to gain indirect marketing whilst also educating the broader community.</p>
    <p>In order to monitor the ‘Blog’, all content will be published by KelvoraPartners on behalf of the adviser. This ensures that all content is relevant, engaging and allows for fair representation of all advisers.</p>
  </div>
  <div class="column column--right-narrow">
    <h2 class="home-feature">Home Page Feature</h2>
    <p class="tight">In order to build a stronger online presence, KelvoraPartners is offering up to 4 ‘Blog’ postigs and up to 5 advisers to be featured on the KelvoraPartners home page.</p>
    <p>You profile will be immediately available to all users who visit the KelvoraPartners homepage which will drive additional traffic to your profile and your credibility.</p>
    <h2 class="section-gap">Comprehensive Statistics</h2>
    <p>KelvoraPartners also allows advisers to track all activity on their account and ‘Adviser Profile’.</p>
    <ul class="stat-list">
      <li>Number of visitors</li>
      <li>Number of appearances in Search</li>
      <li>Number of matched clients</li>
      <li>Number of contacted clients</li>
    </ul>
    <p>KelvoraPartners will provide information on how to improve the performance of your profile.</p>
  </div>

  <svg class="footer-band" viewBox="0 0 564 90" preserveAspectRatio="none" aria-hidden="true">
    <rect width="564" height="90" fill="var(--orange)"/>
    <polygon points="0,0 90,0 40,90 0,90" fill="var(--orange-deep)" opacity=".5"/>
    <rect x="150" y="0" width="14" height="90" fill="var(--orange-light)" opacity=".5"/>
    <rect x="330" y="10" width="30" height="80" fill="var(--orange-light)" opacity=".4"/>
    <rect x="470" y="0" width="10" height="90" fill="var(--orange-deep)" opacity=".4"/>
  </svg>
  <div class="footer-url">www.KelvoraPartners.com.au</div>
</section>

<div class="page-number page-number--three">3</div>
<div class="page-number page-number--four">4</div>

</body>
</html>
```